Redesign Web Page

I am looking for a great re-design and possibly a banner for TrueSpark.us. The site is for an online dating (self-development, online dating) book. The purpose is to drive book sales.

Target Market(s)

Women 18-55

```html
<!DOCTYPE html>
<html lang="en">
<head>
<meta charset="utf-8">
<title>True Spark – online dating made easy</title>
<link href="https://fonts.googleapis.com/css2?family=Open+Sans:wght@400;600;700&family=Tinos:wght@400&display=swap" rel="stylesheet">
<style>
:root{
  --pink:#c0548f;
  --pink-dark:#a3396f;
  --pink-soft:#c86a9c;
  --plum:#8f3a6a;
  --red:#9b1a1a;
  --ink:#2b2b2b;
  --body:#3c3c3c;
  --cream:#f1ede6;
  --cream-light:#f6f4ef;
  --footer:#2d2d2d;
  --white:#fff;
}
*{box-sizing:border-box;margin:0;padding:0}
html,body{width:738px;height:1200px;overflow:hidden}
body{position:relative;background:var(--cream);font-family:"Open Sans",sans-serif;color:var(--body)}
.abs{position:absolute}
.header{left:0;top:0;width:738px;height:54px;background:linear-gradient(#c45f95,#b94f89)}
.logo{left:62px;top:8px;font-family:"Tinos",serif;color:var(--white);font-size:24px;letter-spacing:.5px}
.tagline{left:62px;top:34px;font-family:"Tinos",serif;color:var(--white);font-size:11.5px}
.search{left:485px;top:21px;width:148px;height:13px;background:var(--white);font-size:7px;color:#999;padding:2px 0 0 13px}
.search-btn{left:633px;top:21px;width:39px;height:13px;background:#333;color:var(--white);font-size:7px;text-align:center;line-height:13px}
.nav{left:0;top:54px;width:738px;height:28px;background:linear-gradient(#fff,#ececec);border-bottom:1px solid #d4d4d4;display:flex;padding-left:60px}
.nav a{font-size:8.8px;color:var(--ink);text-decoration:none;padding:0 13px;line-height:28px;border-right:1px solid #ddd}
.nav a.active{background:var(--pink);color:var(--white);padding:0 18px}
.hero{left:0;top:82px;width:738px;height:261px;background:radial-gradient(circle at 35% 40%,#efefef,#d5d5d7 75%)}
.book{left:85px;top:112px;width:165px;height:256px;background:linear-gradient(135deg,#2a2a2a 0 10%,#f2eeee 10% 60%,#c43a3a 60%);border-radius:3px;box-shadow:3px 3px 8px rgba(0,0,0,.35)}
.hero-line{left:307px;font-size:15.5px;letter-spacing:.2px;text-transform:uppercase}
.l1{top:130px;color:var(--plum)}
.l2{top:152px;color:var(--plum)}
.l3{top:180px;color:var(--pink)}
.l4{top:202px;color:var(--pink)}
.paper{left:307px;top:233px;font-size:11.5px;color:#555}
.by{left:307px;top:254px;font-size:8.5px;color:#444}
.buy{left:307px;top:282px;width:125px;height:36px;background:linear-gradient(#cf6aa2,#b24886);border-radius:3px;color:var(--white);font-size:11px;font-weight:600;text-align:center;line-height:36px}
.dots{left:630px;top:314px;display:flex;gap:3px}
.dots span{width:6px;height:6px;border-radius:50%;background:var(--white)}
.dots span.on{border:1.5px solid #333;width:8px;height:8px;margin-top:-1px}
.h2{font-size:13.5px;font-weight:400;color:var(--ink)}
.author-h{left:71px;top:382px}
.author-photo{left:69px;top:405px;width:123px;height:167px;background:linear-gradient(#6a6a6a,#3fb3d6 60%,#2a2a2a)}
.author-text{left:207px;top:405px;width:262px;font-size:7.9px;line-height:12.3px;color:var(--body)}
.more-red{font-size:7.5px;color:var(--red)}
.author-more{left:210px;top:561px}
.signup{left:504px;top:398px;width:158px;height:172px;background:linear-gradient(#c65c97,#b14c87);border-radius:3px;border:1px solid #9e3f76}
.signup h3{position:absolute;left:7px;top:8px;font-size:12.5px;font-weight:600;color:var(--white)}
.field{position:absolute;left:9px;width:137px;height:19px;background:var(--white);border-radius:2px;font-size:6.5px;font-style:italic;color:#888;padding:5px 10px}
.submit{position:absolute;left:97px;top:119px;width:50px;height:17px;background:#111;border-radius:9px;color:var(--white);font-size:8.5px;font-style:italic;text-align:center;line-height:17px}
.fine{position:absolute;left:14px;top:143px;font-family:"Tinos",serif;font-size:7.5px;color:var(--white)}
.tips{left:0;top:592px;width:738px;height:263px;background:var(--cream-light)}
.tips-h{left:69px;top:607px}
.tips-h em{font-style:normal;color:var(--pink-dark)}
.rule{left:69px;top:630px;width:593px;border-top:1px dotted #bbb}
.circle{left:642px;top:606px;width:15px;height:15px;border:1px solid #aaa;border-radius:50%}
.card{top:644px;width:122px}
.card .frame{width:120px;height:112px;background:var(--white);padding:6px;box-shadow:0 0 3px rgba(0,0,0,.12)}
.card .frame div{width:100%;height:100%}
.card h4{font-size:9.5px;font-weight:600;color:var(--ink);margin:9px 0 4px 3px}
.card p{font-size:7.2px;line-height:11px;margin-left:3px}
.card .more-red{margin:5px 0 0 3px}
.col-h{top:879px}
.story .frame{width:177px;height:90px;background:var(--white);padding:6px;box-shadow:0 0 3px rgba(0,0,0,.12)}
.story .frame div{width:100%;height:100%}
.story{top:907px;width:178px}
.story p{font-size:7.3px;line-height:11.1px;margin-top:9px;color:var(--ink)}
.story .cite{color:#c8643c}
.btn{position:absolute;width:58px;height:20px;background:var(--pink-soft);color:var(--white);font-size:7.5px;text-align:center;line-height:20px}
.footer{left:0;top:1123px;width:738px;height:77px;background:linear-gradient(#3a3a3a,#262626)}
.icons{left:73px;top:1146px;display:flex;gap:8px}
.icons span{width:15px;height:15px;border-radius:2px}
.flinks{right:68px;top:1135px;font-size:7.5px;color:#ddd}
.copy{right:68px;top:1153px;font-size:7.5px;color:#ddd}
.x2{right:68px;top:1168px;font-size:7.5px;color:#ddd}
</style>
</head>
<body>
<div class="abs header"></div>
<div class="abs logo">TRUE SPARK</div>
<div class="abs tagline">online dating made easy</div>
<div class="abs search">Enter Key word</div>
<div class="abs search-btn">SEARCH</div>
<nav class="abs nav">
  <a class="active">Home</a><a>The Author</a><a>Blog</a><a>Fan Fair &amp; Fun</a><a>Celeb Endorsements</a><a>Love Stories</a><a>Products &amp; Services</a><a>Contact Us</a>
</nav>
<section class="abs hero" role="img" aria-label="Soft grey background scattered with pink hearts"></section>
<div class="abs book" role="img" aria-label="Book cover of True Spark showing a woman in a red gown"></div>
<div class="abs hero-line l1">Searching for a spark</div>
<div class="abs hero-line l2">I found my glow</div>
<div class="abs hero-line l3">True Spark: Become the Star of</div>
<div class="abs hero-line l4">Online Dating in a Single Week</div>
<div class="abs paper">Paperback</div>
<div class="abs by">by Lena Marlow (Author)</div>
<div class="abs buy">BUY NOW</div>
<div class="abs dots"><span class="on"></span><span></span><span></span><span></span></div>

<h2 class="abs h2 author-h">The Author</h2>
<div class="abs author-photo" role="img" aria-label="Portrait of the author in a turquoise dress"></div>
<p class="abs author-text">Lena Marlow is the author of the self-development guide to online dating—True Spark: become the STAR of online dating in a single week. While Lena spent many years attaining her formal education to become an attorney, she has spent a lifetime becoming herself. She has now mastered the art of fulfillment and become the exceptional woman she was born to be. Her purpose is now to empower other women to find strength in their femininity and fire within themselves. A graduate of Westbrook School of Law and Grant Rowley's Master University and Leadership programs, she can boast achievements in other disciplines as well: becoming a Neuro Linguistic Programming (NLP) practitioner; completing extensive hours training with Daniel Dorne personally (author of The Steady Heart);</p>
<div class="abs more-red author-more">More &gt;&gt;</div>
<form class="abs signup">
  <h3>Free Online Dating Tips</h3>
  <div class="field" style="top:41px">First Name</div>
  <div class="field" style="top:66px">Last Name</div>
  <div class="field" style="top:91px">Your Email</div>
  <div class="submit">SUBMIT</div>
  <div class="fine">Email Marketing by MailNest</div>
</form>

<section class="abs tips"></section>
<h2 class="abs h2 tips-h">Our <em>Tips</em></h2>
<div class="abs rule"></div>
<div class="abs circle"><svg width="13" height="13" viewBox="0 0 13 13"><path d="M5 3.5 8 6.5 5 9.5" fill="none" stroke="#999" stroke-width="1.2"/></svg></div>
<div class="abs card" style="left:81px"><div class="frame"><div role="img" aria-label="Dating tips cover with a group of smiling friends" style="background:linear-gradient(#8a1f4f 55%,#c89a4a)"></div></div><h4>Lovely Tips</h4><p>Curabitur congue lorem massa, quis ultrices nibh rhoncus vel. Nunc quis sapien et nisl ultrices suscipit sit amet tristique lorem.</p><div class="more-red">More ▫</div></div>
<div class="abs card" style="left:230px"><div class="frame"><div role="img" aria-label="Woman with makeup brushes and cosmetics" style="background:linear-gradient(135deg,#c9a58c,#efe4dc)"></div></div><h4>Makeup Tips</h4><p>Curabitur congue lorem massa, quis ultrices nibh rhoncus vel. Nunc quis sapien et nisl ultrices suscipit sit amet tristique lorem.</p><div class="more-red">More ▫</div></div>
<div class="abs card" style="left:378px"><div class="frame"><div role="img" aria-label="Hands typing on a laptop keyboard" style="background:linear-gradient(135deg,#cfcfcf,#4a4a4a)"></div></div><h4>Online Tips</h4><p>Curabitur congue lorem massa, quis ultrices nibh rhoncus vel. Nunc quis sapien et nisl ultrices suscipit sit amet tristique lorem.</p><div class="more-red">More ▫</div></div>
<div class="abs card" style="left:532px"><div class="frame"><div role="img" aria-label="Couple jogging outdoors in the hills" style="background:linear-gradient(#b8c6d4,#7d9370)"></div></div><h4>Health Tips</h4><p>Curabitur congue lorem massa, quis ultrices nibh rhoncus vel. Nunc quis sapien et nisl ultrices suscipit sit amet tristique lorem.</p><div class="more-red">More ▫</div></div>

<h2 class="abs h2 col-h" style="left:67px">Success-Stories</h2>
<h2 class="abs h2 col-h" style="left:277px">Love Stories</h2>
<h2 class="abs h2 col-h" style="left:485px">Best Sellers</h2>
<div class="abs story" style="left:68px"><div class="frame"><div role="img" aria-label="Smiling couple embracing outdoors" style="background:linear-gradient(90deg,#8c9a4c,#d8a27a)"></div></div><p>Carl Silvano, National Ledger and Metro Street Journal best selling author explains, As an author, entrepreneur and personal development coach, it's always refreshing when someone is able to give new insight into a popular topic. Lena Marlow has impressively found a way to combine unique</p></div>
<div class="abs story" style="left:278px"><div class="frame"><div role="img" aria-label="Couple sitting among autumn leaves" style="background:linear-gradient(#c88a2c,#8a5a1e)"></div></div><p>Here Comes The Bride<br>I still can't believe Lena got me to go online! I was totally against online dating; to put myself out to the public like that. I'm a sophisticated, intelligent, classy woman. What if my friends found out? <span class="cite">~Bree–Harbor Town, SC</span></p></div>
<div class="abs story" style="left:485px"><div class="frame"><div role="img" aria-label="Portrait of a bestselling author" style="background:linear-gradient(90deg,#3f8f7d,#c49a82,#3f8f7d)"></div></div><p>Marion Whitfield, author of four #1 National Ledger Best Sellers, "Few things are better than a good sit-down chat with a close girlfriend...especially when she knows what she's talking about. Author Lena Marlow becomes your newest close girlfriend</p></div>
<div class="btn" style="left:68px;top:1079px">MORE &gt;&gt;</div>
<div class="btn" style="left:278px;top:1079px">MORE &gt;&gt;</div>
<div class="btn" style="left:485px;top:1079px">MORE &gt;&gt;</div>

<footer class="abs footer"></footer>
<div class="abs icons" aria-label="Social links">
  <span style="background:#3b5a98"></span><span style="background:#3aa9e0"></span><span style="background:#444"></span><span style="background:#e8901f"></span><span style="background:#c1272d"></span><span style="background:#6b8aa0"></span>
</div>
<div class="abs flinks">Privacy &nbsp;|&nbsp; Terms of Use &nbsp;|&nbsp; Contact Us</div>
<div class="abs copy">© 2014 truespark. All rights reserved</div>
<div class="abs x2">X2</div>
</body>
</html>
```